Fontenot Bayou Grillhouse (Owners Card)

Need a classy, but modern business card. I have included a promotional card for the steakhouse. I need one for myself (the owner) that is more professional.

Target Market(s)

General Public

Industry/Entity Type

Food service

Contact Information for Business Card

Name, business address, phone number, email, logo

Font styles to use
Serif
Sans Serif
Decorative
Script

Requirements
Must have
• My name (Darvel Pruitt), business address (327 Oakmere Street), phone number (510) 493-2615, email (Dpruittkr4@mailvane.example. On the back of the card: Psalms 27 1 The LORD is my light and my salvation— whom shall I fear? The LORD is the stronghold of my life— of whom shall I be afraid? 2 When the wicked advance against me to devour me, it is my enemies and my foes who will stumble and fall. 3 Though an army besiege me, my heart will not fear; though war break out against me, even then I will be confident.
Nice to have
• Something that’s bold, but modern and professional.

```html
<!DOCTYPE html>
<html lang="en">
<head>
<meta charset="utf-8">
<title>Fontenot Bayou Grillhouse – Owner Card</title>
<link rel="stylesheet" href="https://fonts.googleapis.com/css2?family=Cinzel:wght@400;500&family=Poppins:wght@400;500;600&display=swap">
<style>
  :root {
    --backdrop: #36373a;
    --card-black: #0d0d0d;
    --green: #3bb54a;
    --yellow: #b9c23a;
    --orange: #f7a21b;
    --red: #ec1d25;
    --white: #ffffff;
    --soft-white: #e9e9e9;
  }
  * { margin: 0; padding: 0; box-sizing: border-box; }
  html, body { width: 1200px; height: 801px; overflow: hidden; }
  body {
    background: var(--backdrop);
    font-family: "Poppins", sans-serif;
    position: relative;
  }
  .card {
    position: absolute;
    left: 290px;
    width: 620px;
    height: 354px;
    border-radius: 18px;
    box-shadow: 0 10px 26px rgba(0,0,0,0.45);
    overflow: hidden;
  }
  /* Back: scripture */
  .card-back {
    top: 30px;
    background: linear-gradient(60deg, var(--green) 8%, var(--yellow) 38%, var(--orange) 62%, var(--red) 92%);
    color: var(--white);
    padding: 40px 44px;
    font-weight: 600;
    font-size: 15.5px;
    line-height: 1.42;
  }
  .scripture-title { margin-bottom: 2px; }
  .verse { padding-left: 18px; text-indent: -18px; margin-bottom: 16px; }
  .verse .num { display: inline-block; width: 18px; text-indent: 0; }
  /* Front: contact */
  .card-front {
    top: 417px;
    background: var(--card-black);
    display: flex;
    align-items: center;
  }
  .brand {
    width: 330px;
    display: flex;
    flex-direction: column;
    align-items: center;
    justify-content: center;
    gap: 10px;
    padding-top: 40px;
  }
  .brand-dot {
    width: 14px; height: 14px; border-radius: 50%;
    background: var(--orange);
  }
  .brand-name {
    font-family: "Cinzel", serif;
    font-weight: 500;
    font-size: 25px;
    color: var(--orange);
    text-align: center;
    line-height: 1.25;
    letter-spacing: 0.5px;
  }
  .divider {
    width: 1px;
    height: 200px;
    background: var(--soft-white);
    margin-top: 30px;
  }
  .contact {
    padding-left: 32px;
    color: var(--soft-white);
    margin-top: -30px;
  }
  .owner-name {
    font-family: "Cinzel", serif;
    font-size: 29px;
    font-weight: 400;
    background: linear-gradient(90deg, var(--green), var(--orange) 55%, var(--red));
    -webkit-background-clip: text;
    background-clip: text;
    color: transparent;
    line-height: 1.1;
  }
  .owner-role {
    font-size: 12px;
    letter-spacing: 1px;
    margin: 2px 0 16px 40px;
  }
  .contact-line {
    display: flex;
    align-items: center;
    gap: 8px;
    font-size: 13.5px;
    margin-bottom: 7px;
    padding-left: 30px;
  }
  .contact-line svg { width: 14px; height: 14px; flex: none; }
  .phone-line { font-size: 15px; letter-spacing: 2px; }
  .address {
    font-size: 16px;
    margin-top: 16px;
    padding-left: 46px;
  }
</style>
</head>
<body>

<section class="card card-back" aria-label="Card back with Psalm 27">
  <p class="scripture-title">Psalms 27</p>
  <p class="verse"><span class="num">1</span>The LORD is my light and my salvation— whom shall I fear? The LORD is the stronghold of my life— of whom shall I be afraid?</p>
  <p class="verse"><span class="num">2</span>When the wicked advance against me to devour me, it is my enemies and my foes who will stumble and fall.</p>
  <p class="verse"><span class="num">3</span>Though an army besiege me, my heart will not fear; though war break out against me, even then I will be confident.</p>
</section>

<section class="card card-front" aria-label="Card front with owner contact details">
  <div class="brand">
    <span class="brand-dot"></span>
    <p class="brand-name">Fontenot Bayou<br>Grillhouse</p>
  </div>
  <div class="divider"></div>
  <div class="contact">
    <h1 class="owner-name">DARVEL PRUITT</h1>
    <p class="owner-role">OWNER</p>
    <p class="contact-line phone-line">
      <svg viewBox="0 0 24 24"><path fill="#f7a21b" d="M6.6 10.8a15.1 15.1 0 0 0 6.6 6.6l2.2-2.2a1 1 0 0 1 1-.25 11.4 11.4 0 0 0 3.6.57 1 1 0 0 1 1 1V20a1 1 0 0 1-1 1A17 17 0 0 1 3 4a1 1 0 0 1 1-1h3.5a1 1 0 0 1 1 1c0 1.25.2 2.45.57 3.57a1 1 0 0 1-.25 1z"/></svg>
      (510) 493-2615
    </p>
    <p class="contact-line">
      <svg viewBox="0 0 24 24"><rect x="2" y="5" width="20" height="14" fill="#3bb54a"/><path d="M2 5l10 8 10-8" fill="none" stroke="#ec1d25" stroke-width="2"/></svg>
      Dpruittkr4@mailvane.example
    </p>
    <p class="contact-line">
      <svg viewBox="0 0 24 24"><circle cx="12" cy="12" r="10" fill="none" stroke="#f7a21b" stroke-width="2"/><path d="M2 12h20M12 2c3 3 3 17 0 20M12 2c-3 3-3 17 0 20" fill="none" stroke="#3bb54a" stroke-width="1.6"/></svg>
      fontenotbayou.example
    </p>
    <p class="address">327 Oakmere Street</p>
  </div>
</section>

</body>
</html>
```